Product Label for Health Supplement

Design a product label to go on the jar. The product is a health supplement super-food called Moringa oleifera (Moringa leaf).

This product will be sold online at verdalune.com.au and in health-food stores. For inspiration, you can see Verdalune's 2 products on verdalune.com.au which are in a jar size similar to this new product.

The label needs to be attractive and feels natural and healthy.

A content template has been prepared for you. Please use all the content from the template in your design concept. There is no need to add new text. Please keep the text provided in the template.

The label has been setout in left, front, and right sides.
Here is the link to the template (also attached to the design brief) https://www.plankboard.net/file/4Rt9sLwQe2XbNcVm8YhKdA/Untitled?type=design&node-id=0%3A1&t=PzQ7mTrGhJ3kLwXn-1

Required Label Design Specifications:
Max Length: 275mm
Max Height: 70mm
DPI: 300 (at least)
Colour: CMYK
Minimum font: 5pt
Bleed: 1.5mm
Safe zone: 3mm from edge all around.

Once approved, the design will need to be delivered in CMYK color and in PDF format.

The Art Guidelines have been attached.

```html
<!DOCTYPE html>
<html lang="en">
<head>
<meta charset="utf-8">
<title>Verdalune Organic Moringa – Front Label</title>
<link rel="stylesheet" href="https://fonts.googleapis.com/css2?family=Lora:wght@500&family=Open+Sans:ital,wght@0,600;0,700;0,800;1,700&family=Kaushan+Script&display=swap">
<style>
  :root {
    --page: #ffffff;
    --label: #ffffff;
    --label-edge: #e4e8e0;
    --green-dark: #0d6b34;
    --green-leaf: #8cc63f;
    --green-lime: #b5d333;
    --ink: #1f2a24;
    --red: #e5212a;
    --plant: #9bd14c;
  }
  * { margin: 0; padding: 0; box-sizing: border-box; }
  html, body { width: 1200px; height: 1200px; overflow: hidden; background: var(--page); }
  .label {
    position: absolute; left: 85px; top: 193px; width: 1030px; height: 814px;
    background: var(--label); border: 1px solid var(--label-edge);
    font-family: "Open Sans", Arial, sans-serif; color: var(--ink); overflow: hidden;
  }
  .hero { position: absolute; left: 0; top: 0; width: 1030px; height: 814px; }
  .brand {
    position: absolute; left: 0; width: 1030px; top: 52px; text-align: center;
    font-family: "Lora", Georgia, serif; font-weight: 500; font-size: 62px; line-height: 1;
    color: var(--ink); letter-spacing: 1px;
  }
  .lab-badge { position: absolute; left: 860px; top: 36px; width: 120px; text-align: center; }
  .lab-badge svg { width: 56px; height: 100px; }
  .lab-badge span { display: block; font-size: 18px; font-weight: 700; color: var(--ink); margin-top: 4px; }
  .tagline {
    position: absolute; left: 70px; top: 185px; width: 240px; text-align: center;
    transform: rotate(-38deg); line-height: 1;
    font-family: "Kaushan Script", cursive; font-size: 46px; color: var(--red);
  }
  .title { position: absolute; left: 200px; width: 600px; text-align: center; color: #fff; font-weight: 800; line-height: 1; }
  .title-organic { top: 250px; font-size: 70px; letter-spacing: 1px; }
  .title-moringa { top: 318px; font-size: 100px; letter-spacing: 2px; }
  .title-sub { top: 424px; font-size: 33px; font-weight: 700; font-style: italic; color: var(--green-lime); }
  .features { position: absolute; left: 290px; top: 533px; list-style: none; }
  .features li {
    display: flex; align-items: center; gap: 16px; height: 54px;
    font-size: 31px; font-weight: 700; font-style: italic; color: var(--ink);
  }
  .features svg { width: 36px; height: 36px; flex: none; }
  .serves {
    position: absolute; left: 86px; top: 684px; width: 148px; height: 76px;
    background: var(--green-dark); border-right: 10px solid var(--green-leaf);
    color: #fff; padding: 4px 0 0 10px; line-height: 1.05;
  }
  .serves strong { display: block; font-size: 34px; font-weight: 800; }
  .serves span { font-size: 24px; font-weight: 600; }
  .net-weight { position: absolute; left: 370px; top: 712px; font-size: 26px; line-height: 1; color: var(--ink); font-weight: 600; }
  .net-weight strong { font-size: 34px; font-weight: 800; }
  .plant-art {
    position: absolute; left: 838px; top: 420px; width: 150px; height: 330px;
    border-radius: 75px 75px 40px 40px;
    background: linear-gradient(180deg, #c4e58a 0%, var(--plant) 60%, #7fbf3a 100%);
    opacity: 0.85;
  }
</style>
</head>
<body>
  <main class="label">
    <svg class="hero" viewBox="0 0 1030 814" aria-hidden="true">
      <path d="M100 340 C 200 200 420 150 600 162 C 800 175 900 260 880 360 C 865 440 800 500 720 530 C 820 470 850 400 840 340 C 820 250 700 200 560 196 C 400 192 220 240 100 340 Z" fill="var(--green-leaf)"/>
      <ellipse cx="530" cy="369" rx="320" ry="145" fill="var(--green-dark)" stroke="#ffffff" stroke-width="10"/>
      <path d="M300 722 C 340 770 420 790 560 786 C 700 782 800 750 840 700" fill="none" stroke="var(--green-leaf)" stroke-width="8" stroke-linecap="round"/>
    </svg>

    <div class="brand">verdalune</div>

    <div class="lab-badge">
      <svg viewBox="0 0 56 100" aria-hidden="true">
        <circle cx="24" cy="8" r="4" fill="var(--green-dark)"/>
        <circle cx="32" cy="20" r="3" fill="var(--green-dark)"/>
        <path d="M19 32 H37 V50 L52 92 H4 L19 50 Z" fill="none" stroke="var(--green-dark)" stroke-width="4" stroke-linejoin="round"/>
        <path d="M12 68 H44 L50 89 H6 Z" fill="var(--green-dark)"/>
      </svg>
      <span>Lab Tested</span>
    </div>

    <div class="tagline">Our Purest</div>
    <div class="title title-organic">ORGANIC</div>
    <div class="title title-moringa">MORINGA</div>
    <div class="title title-sub">Premium-Grade Leaf Powder</div>

    <ul class="features">
      <li><svg viewBox="0 0 34 34" aria-hidden="true"><circle cx="17" cy="17" r="15" fill="none" stroke="var(--green-leaf)" stroke-width="3"/><path d="M10 17 L15 22 L24 12" fill="none" stroke="var(--green-dark)" stroke-width="3.5" stroke-linecap="round"/></svg>Naturally Air-Dried</li>
      <li><svg viewBox="0 0 34 34" aria-hidden="true"><circle cx="17" cy="17" r="15" fill="none" stroke="var(--green-leaf)" stroke-width="3"/><path d="M10 17 L15 22 L24 12" fill="none" stroke="var(--green-dark)" stroke-width="3.5" stroke-linecap="round"/></svg>No Irradiation/Chemicals</li>
      <li><svg viewBox="0 0 34 34" aria-hidden="true"><circle cx="17" cy="17" r="15" fill="none" stroke="var(--green-leaf)" stroke-width="3"/><path d="M10 17 L15 22 L24 12" fill="none" stroke="var(--green-dark)" stroke-width="3.5" stroke-linecap="round"/></svg>No Cheap ‘Fillers’</li>
    </ul>

    <div class="serves"><strong>30</strong><span>Serves</span></div>
    <div class="net-weight"><strong>150G</strong> Net Weight</div>

    <div class="plant-art" role="img" aria-label="Illustration of a green moringa sprig with round leaves"></div>
  </main>
</body>
</html>
```